依頼概要
■ 依頼の目的/概要

育毛剤・シャンプーのランキングサイトのデザインをお願い致します。

■ デザインへの要望

・イメージ画像として人間(できれば女性)の写真もしくは、イラストを使用してください。
・ランキングの順位と商品の特徴(写真や文字)をメインに強調したデザインにしてください。
・サイトを訪れた際に育毛剤・シャンプーのランキングサイトであることがわかるようにしてください。
・ランキングの上位3件ほどがはっきりと見えるようにしてください。
・ランキングサイトの参考として以下に、いくつか参考URLを記載しておきます。
・http://xn--7pqt52fkwa.net/
・http://xn--7pqt52fzmc.com/
・http://www.tyvalpeq.org/
・http://www.sorafumikiri-junban.com/
・http://tanepoka.v-nest.net/

■ 納品ファイルの希望

フォトショップ形式(.psd形式)でお願い致します。

■ 利用用途

主に育毛剤・シャンプーのランキングサイトに使用させて頂きます。

■ 進め方

弊社の希望するイメージに近い提案を1つ(場合によって複数)選択させて頂きます。希望に近づけるために、修正要望を個別にさせて頂くこともあります。コンペ方式のため、修正後に当選されない場合も、どうかご了承ください。

■ その他/注意点

選択させて頂いたデザインの著作権(財産権)等の扱いはBravoly利用規約に従い、弊社に譲渡をお願いします。フォントや画像素材などを利用する場合は上記利用用途に使用できることを確認し、第三者の知的財産権等に注意して下さい。
補足:
今回はサイトのトップページのデザインのみでも結構です。

トップページに必要な内容ですが、
サイトを訪れた際に育毛剤ランキングへのリンクと、シャンプーランキングへのリンクとランキングの上位3位までは、表示できるようにして下さい。
(最初に表示されるのは育毛剤ランキングでお願い致します)

トップページの項目としては以下のようにお願い致します。
ナビゲーション(育毛剤ランキングへのリンクとシャンプーランキングへのリンク), 商品名, 商品の特徴を表した一文(※), 価格, 容量, 男女兼用かどうか, 評判(☆を使うなどわかりやすく), 販売サイトへのリンク

サイトのロゴや基調となる色の指定は、暖色系を基調としてください。

※商品の特徴を表した一文の例文と致しましては、「発毛率No.1の育毛サプリメント!」や「発毛率96%、平均1~2ヶ月の発毛スピード!」また、「30日で満足できないなら全額返金!」などです。
■ 選んだ理由

今回minteluさんの提案を当選とさせて頂いた理由と致しましては、
要望に対してイメージ通りの提案をして下さったことです。

修正依頼に対しても誠意をもって応じて下さったので、
この提案を当選とさせて頂きました。

■ 提案者全員へのお礼・コメント

皆様、ご提案ありがとうございました。
弊社としましても非常に選考に苦労いたしました。

落選された方には残念な結果にはなったのですが、
今後とも機会がございましたら、よろしくお願い致します。

```html
<!DOCTYPE html>
<html lang="ja">
<head>
<meta charset="utf-8">
<title>育毛剤・シャンプーのランキングサイト</title>
<link href="https://fonts.googleapis.com/css2?family=Noto+Sans+JP:wght@400;500;700&display=swap" rel="stylesheet">
<style>
:root{
  --pink:#e8667d;
  --pink-deep:#d9475f;
  --pink-soft:#f7c3cc;
  --pink-pale:#fdeef1;
  --text:#444;
  --muted:#8a8a8a;
  --line:#e6d6d9;
  --bg:#ffffff;
  --page:#f4f1ef;
}
*{box-sizing:border-box;margin:0;padding:0}
html,body{width:867px;height:1200px;overflow:hidden;background:var(--page)}
body{font-family:"Noto Sans JP",sans-serif;color:var(--text)}
.site{width:867px;height:1200px;background:var(--bg);position:relative}
.site-header{height:150px;position:relative;padding:30px 0 0 40px}
.brand{display:flex;align-items:center;gap:10px}
.brand-mark{width:28px;height:28px;border-radius:50%;background:var(--pink);flex:none}
.brand-name{font-size:24px;font-weight:700;color:var(--pink-deep);letter-spacing:.02em;white-space:nowrap}
.brand-lead{margin:12px 0 0 38px;width:500px;font-size:11px;line-height:1.7;color:var(--muted)}
.hero-photo{position:absolute;right:40px;top:14px;width:220px;height:130px;
  background:linear-gradient(120deg,#f6e4dc,#e9cfc4 55%,#d9b7a8);}
.global-nav{display:flex;background:var(--pink);height:32px}
.global-nav a{flex:1;color:#fff;text-decoration:none;font-size:13px;font-weight:700;
  display:flex;align-items:center;justify-content:center;border-right:1px solid rgba(255,255,255,.5)}
.global-nav a:last-child{border-right:0}
.breadcrumb{padding:9px 40px;font-size:10px;color:var(--muted);border-bottom:1px solid var(--line)}
.rankings{display:flex;gap:27px;padding:22px 40px 0}
.ranking{flex:1;min-width:0}
.ranking-title{font-size:22px;font-weight:700;color:var(--pink-deep);line-height:1.4;padding-bottom:6px;
  border-bottom:3px solid var(--pink);margin-bottom:12px}
.rank-item{display:flex;height:136px;margin-bottom:8px;border:1px solid var(--line);background:#fff;overflow:hidden}
.rank-badge{width:44px;flex:none;background:var(--pink);color:#fff;display:flex;flex-direction:column;
  align-items:center;justify-content:center;gap:4px}
.rank-badge svg{width:20px;height:14px}
.rank-num{font-size:28px;font-weight:700;line-height:1}
.rank-body{flex:1;padding:7px 10px 7px;display:flex;flex-direction:column;position:relative;min-width:0}
.rank-catch{font-size:9px;line-height:1.4;color:var(--pink-deep);width:220px;white-space:nowrap;overflow:hidden}
.rank-name{font-size:16px;line-height:1.4;font-weight:700;margin-top:1px;color:#333}
.rank-sub{font-size:9px;line-height:1.4;color:var(--muted);border-bottom:1px dotted var(--line);padding-bottom:2px;width:200px}
.rank-spec{font-size:9px;line-height:1.4;margin-top:3px;color:var(--text)}
.stars{color:#f0a21c;letter-spacing:1px}
.rank-buttons{display:flex;gap:8px;margin-top:auto;width:220px}
.btn{flex:1;height:16px;background:var(--pink-soft);color:var(--pink-deep);font-size:8px;
  display:flex;align-items:center;justify-content:center;border-radius:2px}
.btn.primary{background:var(--pink);color:#fff}
.product-photo{position:absolute;right:10px;top:9px;width:78px;height:116px;
  background:linear-gradient(180deg,#f4f1ea,#dcd7cc)}
.product-photo.green{background:linear-gradient(180deg,#f2f4ee,#c9d6b5)}
.product-photo.gold{background:linear-gradient(180deg,#efe3b8,#c49a3a)}
.product-photo.dark{background:linear-gradient(180deg,#4a4a4a,#1f1f1f)}
.product-photo.red{background:linear-gradient(180deg,#d9474a,#a21d22)}
.more-link{display:flex;align-items:center;justify-content:center;margin-top:12px;height:38px;
  background:var(--pink);color:#fff;font-size:13px;font-weight:700;border-radius:4px}
.site-footer{position:absolute;left:0;right:0;bottom:0;height:56px;border-top:3px solid var(--pink);
  display:flex;justify-content:space-between;align-items:center;padding:0 40px;font-size:10px;color:var(--muted)}
.footer-links{display:flex;gap:14px}
</style>
</head>
<body>
<div class="site">
  <header class="site-header">
    <div class="brand">
      <span class="brand-mark"></span>
      <span class="brand-name">育毛剤・シャンプーのランキングサイト</span>
    </div>
    <p class="brand-lead">育毛剤やシャンプーを成分と効果で比較し、人気順にご紹介します。口コミ評価や価格、容量もひと目でわかるので、自分にぴったりの商品選びにお役立てください。</p>
    <div class="hero-photo" role="img" aria-label="髪に手を添えてほほえむ女性の写真"></div>
  </header>

  <nav class="global-nav">
    <a href="#">TOP</a>
    <a href="#">育毛剤人気ランキング</a>
    <a href="#">シャンプー人気ランキング</a>
    <a href="#">育毛剤ガイド</a>
  </nav>
  <div class="breadcrumb">TOP ＞ シャンプー・育毛剤のランキングサイトTOP</div>

  <main class="rankings">
    <section class="ranking">
      <h2 class="ranking-title">育毛剤人気ランキング</h2>
      <article class="rank-item"><div class="rank-badge"><svg viewBox="0 0 20 14"><path d="M1 13h18L17 3l-4 5-3-7-3 7-4-5z" fill="#fff"/></svg><span class="rank-num">1</span></div>
        <div class="rank-body"><p class="rank-catch">発毛率96%、平均1〜2ヶ月の発毛スピード！</p><h3 class="rank-name">ルミナシャンプー</h3><p class="rank-sub">SORA PLUS</p>
          <p class="rank-spec">価格：3,800円<br>容量：300ml<br>男女兼用<br>評判：<span class="stars">★★★★★</span></p>
          <div class="rank-buttons"><span class="btn">詳細を見る</span><span class="btn primary">公式サイトへ</span></div>
          <div class="product-photo" role="img" aria-label="白いボトルの商品写真"></div></div></article>
      <article class="rank-item"><div class="rank-badge"><svg viewBox="0 0 20 14"><path d="M1 13h18L17 3l-4 5-3-7-3 7-4-5z" fill="#fff"/></svg><span class="rank-num">2</span></div>
        <div class="rank-body"><p class="rank-catch">30日で満足できないなら全額返金！</p><h3 class="rank-name">ルミナシャンプー</h3><p class="rank-sub">SORA PLUS</p>
          <p class="rank-spec">価格：3,800円<br>容量：300ml<br>男女兼用<br>評判：<span class="stars">★★★★☆</span></p>
          <div class="rank-buttons"><span class="btn">詳細を見る</span><span class="btn primary">公式サイトへ</span></div>
          <div class="product-photo green" role="img" aria-label="白と緑のボトルの商品写真"></div></div></article>
      <article class="rank-item"><div class="rank-badge"><svg viewBox="0 0 20 14"><path d="M1 13h18L17 3l-4 5-3-7-3 7-4-5z" fill="#fff"/></svg><span class="rank-num">3</span></div>
        <div class="rank-body"><p class="rank-catch">発毛率No.1の育毛サプリメント！</p><h3 class="rank-name">ルミナシャンプー</h3><p class="rank-sub">SORA PLUS</p>
          <p class="rank-spec">価格：3,800円<br>容量：300ml<br>男女兼用<br>評判：<span class="stars">★★★★☆</span></p>
          <div class="rank-buttons"><span class="btn">詳細を見る</span><span class="btn primary">公式サイトへ</span></div>
          <div class="product-photo gold" role="img" aria-label="金色のボトルの商品写真"></div></div></article>
      <article class="rank-item"><div class="rank-badge"><span class="rank-num">4</span></div>
        <div class="rank-body"><p class="rank-catch">頭皮にやさしい天然由来成分を配合！</p><h3 class="rank-name">ルミナシャンプー</h3><p class="rank-sub">SORA PLUS</p>
          <p class="rank-spec">価格：3,800円<br>容量：300ml<br>男女兼用<br>評判：<span class="stars">★★★☆☆</span></p>
          <div class="rank-buttons"><span class="btn">詳細を見る</span><span class="btn primary">公式サイトへ</span></div>
          <div class="product-photo dark" role="img" aria-label="黒いポンプボトルの商品写真"></div></div></article>
      <article class="rank-item"><div class="rank-badge"><span class="rank-num">5</span></div>
        <div class="rank-body"><p class="rank-catch">毎日のケアでハリとコシのある髪へ！</p><h3 class="rank-name">ルミナシャンプー</h3><p class="rank-sub">SORA PLUS</p>
          <p class="rank-spec">価格：3,800円<br>容量：300ml<br>男女兼用<br>評判：<span class="stars">★★★☆☆</span></p>
          <div class="rank-buttons"><span class="btn">詳細を見る</span><span class="btn primary">公式サイトへ</span></div>
          <div class="product-photo red" role="img" aria-label="赤いボトルの商品写真"></div></div></article>
      <a class="more-link">詳細な育毛剤人気ランキングはこちら</a>
    </section>

    <section class="ranking">
      <h2 class="ranking-title">シャンプー人気ランキング</h2>
      <article class="rank-item"><div class="rank-badge"><svg viewBox="0 0 20 14"><path d="M1 13h18L17 3l-4 5-3-7-3 7-4-5z" fill="#fff"/></svg><span class="rank-num">1</span></div>
        <div class="rank-body"><p class="rank-catch">発毛率96%、平均1〜2ヶ月の発毛スピード！</p><h3 class="rank-name">ルミナシャンプー</h3><p class="rank-sub">SORA PLUS</p>
          <p class="rank-spec">価格：3,800円<br>容量：300ml<br>男女兼用<br>評判：<span class="stars">★★★★★</span></p>
          <div class="rank-buttons"><span class="btn">詳細を見る</span><span class="btn primary">公式サイトへ</span></div>
          <div class="product-photo" role="img" aria-label="白いボトルの商品写真"></div></div></article>
      <article class="rank-item"><div class="rank-badge"><svg viewBox="0 0 20 14"><path d="M1 13h18L17 3l-4 5-3-7-3 7-4-5z" fill="#fff"/></svg><span class="rank-num">2</span></div>
        <div class="rank-body"><p class="rank-catch">30日で満足できないなら全額返金！</p><h3 class="rank-name">ルミナシャンプー</h3><p class="rank-sub">SORA PLUS</p>
          <p class="rank-spec">価格：3,800円<br>容量：300ml<br>男女兼用<br>評判：<span class="stars">★★★★☆</span></p>
          <div class="rank-buttons"><span class="btn">詳細を見る</span><span class="btn primary">公式サイトへ</span></div>
          <div class="product-photo green" role="img" aria-label="白と緑のボトルの商品写真"></div></div></article>
      <article class="rank-item"><div class="rank-badge"><svg viewBox="0 0 20 14"><path d="M1 13h18L17 3l-4 5-3-7-3 7-4-5z" fill="#fff"/></svg><span class="rank-num">3</span></div>
        <div class="rank-body"><p class="rank-catch">発毛率No.1の育毛サプリメント！</p><h3 class="rank-name">ルミナシャンプー</h3><p class="rank-sub">SORA PLUS</p>
          <p class="rank-spec">価格：3,800円<br>容量：300ml<br>男女兼用<br>評判：<span class="stars">★★★★☆</span></p>
          <div class="rank-buttons"><span class="btn">詳細を見る</span><span class="btn primary">公式サイトへ</span></div>
          <div class="product-photo gold" role="img" aria-label="金色のボトルの商品写真"></div></div></article>
      <article class="rank-item"><div class="rank-badge"><span class="rank-num">4</span></div>
        <div class="rank-body"><p class="rank-catch">頭皮にやさしい天然由来成分を配合！</p><h3 class="rank-name">ルミナシャンプー</h3><p class="rank-sub">SORA PLUS</p>
          <p class="rank-spec">価格：3,800円<br>容量：300ml<br>男女兼用<br>評判：<span class="stars">★★★☆☆</span></p>
          <div class="rank-buttons"><span class="btn">詳細を見る</span><span class="btn primary">公式サイトへ</span></div>
          <div class="product-photo dark" role="img" aria-label="黒いポンプボトルの商品写真"></div></div></article>
      <article class="rank-item"><div class="rank-badge"><span class="rank-num">5</span></div>
        <div class="rank-body"><p class="rank-catch">毎日のケアでハリとコシのある髪へ！</p><h3 class="rank-name">ルミナシャンプー</h3><p class="rank-sub">SORA PLUS</p>
          <p class="rank-spec">価格：3,800円<br>容量：300ml<br>男女兼用<br>評判：<span class="stars">★★★☆☆</span></p>
          <div class="rank-buttons"><span class="btn">詳細を見る</span><span class="btn primary">公式サイトへ</span></div>
          <div class="product-photo red" role="img" aria-label="赤いボトルの商品写真"></div></div></article>
      <a class="more-link">詳細なシャンプー人気ランキングはこちら</a>
    </section>
  </main>

  <footer class="site-footer">
    <div class="footer-links"><span>育毛剤について</span><span>運営者情報</span><span>免責事項</span><span>サイトマップ</span><span>お問い合わせ</span></div>
    <span>Copyright © 育毛剤・シャンプーのランキングサイト All Rights Reserved.</span>
  </footer>
</div>
</body>
</html>
```